Construction Company informative web page

Torvell Builders is a new company that combine Project Manager and kitchen & bath design with Interior remodeling for houses or business (commercial and residential construction)
We want to show our reviews, portafolio and background experience
Updates

Reason: I would like to have the time to interact with the favorite designers to fine tune the website also I'd like to see more designs

Hello Everybody,

Thank you for your time, please make the corrections shown below:

Pages:

1. Home:

1.  Includes a welcome and a briefly background:

2. Right side vertically show a few reviews with the option read more to open it, just the Name and last name, city and review (no start ratings)

3. Facebook and youtube link

4. Left side below shows 4 slides show with pictures and titles:

1. Kitchen Design

2. Bath Design

3. General Remodeling

4. Commercial Projects

2. About Us:

Our Professionals:

Torvell Builders Project Manager  is responsible to set the project schedule, request materials  and coordinate the delivery on time.  The Project Manager focus is ensuring  the best customer satisfaction in every step of the project until the final product is completed.

The Designer gives you the best ideas in 3D format,   getting the best lay out possible.  understanding your needs, defining your unique style putting together all your requirements and ideas to make the best match for you, making sure you get the best products within your budget

Torvell Builders have a high quality group of trade specialist; plumbers, electricians and installers. Our crew is pleasant to work with,  safety and cleaning values  and very detailed oriented

Our Core Values

As our slogan your project is our business, well we really mean it our job is not just to do the job is to guaranteed a pleasant experience with great costumer service, communication, quality, in time and within your budget

 

1. Services:

1. Commercial

2. Residential

2. Portafolio:  Separated pictures in each project, I want to have a brief description in each picture

1. Kitchen Design

2. Bath Design

3. General Remodeling

4. Commercial Projects

 

1. Contact Us:  

1. Project Management Department:

Contact Person: Rhonda Kestling

Email: rhonda@torvellbuilders.com

2. Office Management Department:

Contact Person: Lou Brambery

Email: info@torvellbuilders.com

 

Please try to pick design style shown in business card to match a little bit. Keep the color tones

I want the logo in the upper left corner and a very nice picture with a kitchen (warm colors)mostly American northeast style like the main pic of the web.

I want the web page is able to be fully open in computers, tablets and cellphones

Please send me an email to torvellbuilders1@mailnest.com so I can send you my logo and any other information to be incorporated

Thank you

Hello Everybody,

Thank you for your time, please make the corrections accordingly:

Pages:

1. Home: Includes a welcome and a briefly say something about our background 

Hello, I just upload my logo and my business card so you can adjust your designs

Please presented responsive format

I want coding the webpage too

Please read carefully my last update

Thank you so much!                                   

Industry/Entity Type

Residential

Requirements
Nice to have
• Should it has a Newsletter subscription with the email at the bottom of the home page
In contact page: A box "Contact us for a free estimate"

```html
<!DOCTYPE html>
<html lang="en">
<head>
<meta charset="utf-8">
<title>Torvell Builders</title>
<link href="https://fonts.googleapis.com/css2?family=Marcellus+SC&family=Open+Sans:ital,wght@0,300;0,400;0,600;1,400&display=swap" rel="stylesheet">
<style>
:root{
  --maroon:#7a2627;
  --maroon-dark:#5a1414;
  --cream:#f4eddc;
  --cream-light:#f7f1e3;
  --menu:#efe4cf;
  --gold:#f1d8a4;
  --tan:#c99c76;
  --sand:#dcb995;
  --ink:#333;
  --white:#fff;
}
*{margin:0;padding:0;box-sizing:border-box}
html,body{width:1200px;height:994px;overflow:hidden}
body{background:var(--cream);font-family:"Open Sans",sans-serif;color:var(--ink);position:relative}
.header-band{position:absolute;left:0;top:0;width:1200px;height:120px;background:var(--maroon)}
.header-stripes{position:absolute;left:0;top:120px;width:1200px;height:14px;
  background:linear-gradient(var(--tan) 0 3px,var(--maroon) 3px 6px,var(--sand) 6px 9px,#e9d6b6 9px 14px)}
.brand{position:absolute;left:268px;top:20px;width:150px;height:150px;border-radius:50%;background:var(--maroon);
  display:flex;align-items:center;justify-content:center;text-align:center}
.brand-name{font-family:"Marcellus SC",serif;color:var(--cream);font-size:19px;line-height:1.15}
.tagline{position:absolute;left:421px;top:103px;font-family:"Marcellus SC",serif;font-size:13px;color:var(--cream)}
.phone{position:absolute;left:864px;top:98px;font-family:"Marcellus SC",serif;font-size:18px;color:var(--cream);display:flex;align-items:center;gap:3px}
.main-nav{position:absolute;left:450px;top:0;width:533px;height:67px;background:var(--cream-light);display:flex;align-items:flex-end;border-left:2px solid var(--maroon-dark)}
.main-nav a{font-family:"Marcellus SC",serif;font-size:17px;color:var(--maroon-dark);text-decoration:none;padding:0 8px 9px;height:67px;display:flex;align-items:flex-end}
.main-nav a.active{background:var(--maroon-dark);color:var(--cream);padding:0 10px 9px}
.main-nav a.open{background:var(--menu)}
.submenu{position:absolute;left:594px;top:67px;width:123px;height:65px;background:var(--menu)}
.submenu a{display:block;font-family:"Marcellus SC",serif;font-size:17px;color:var(--maroon-dark);text-decoration:none;padding:7px 0 0 11px;height:31px}
.hero{position:absolute;left:272px;top:147px;width:709px;height:310px;
  background:linear-gradient(180deg,#6b3a25 0%,#8a4c2e 35%,#c98f60 65%,#5a2f1f 100%);box-shadow:0 1px 3px rgba(0,0,0,.35)}
.hero-dots{position:absolute;right:14px;bottom:5px;display:flex;gap:4px}
.hero-dots span{width:12px;height:12px;border-radius:50%;background:var(--maroon)}
.hero-dots span.on{background:var(--cream)}
.banner{position:absolute;left:272px;top:472px;width:709px;height:42px;background:var(--maroon);box-shadow:0 1px 3px rgba(0,0,0,.3);
  font-family:"Marcellus SC",serif;color:var(--gold);font-size:17px;text-align:center;line-height:42px}
.estimate{position:absolute;left:272px;top:523px;width:709px;height:80px;background:var(--white);box-shadow:0 1px 3px rgba(0,0,0,.3);text-align:center}
.estimate h2{font-weight:300;font-size:28px;color:var(--maroon);margin-top:10px;line-height:36px}
.estimate p{font-weight:300;font-size:18px;color:#444;line-height:22px}
.features{position:absolute;left:272px;top:614px;width:709px;height:289px;background:var(--white);box-shadow:0 1px 3px rgba(0,0,0,.3)}
.feature{position:absolute;top:18px}
.feature h3{font-weight:300;font-size:19px;color:#333;line-height:26px}
.feature .photo{display:block;box-shadow:0 1px 3px rgba(0,0,0,.45)}
.feature p{font-size:11px;line-height:13px;color:#222;margin-top:14px}
.feature .more{position:absolute;font-size:11px;color:var(--maroon);text-decoration:underline}
.services{left:29px;width:181px}
.work{left:238px;width:208px}
.reviews{left:474px;width:207px}
.quote{font-style:italic;font-size:10.5px!important;padding:0 3px}
.author{text-align:right;font-size:11px;line-height:14px;margin-top:9px;padding-right:4px}
.author b{font-weight:600}
.footer{position:absolute;left:275px;top:917px;width:708px;height:77px;background:var(--maroon)}
.footer-nav{position:absolute;left:27px;top:14px;display:flex;gap:11px}
.footer-nav a{font-family:"Marcellus SC",serif;font-size:13px;color:var(--cream);text-decoration:none}
.copyright{position:absolute;left:27px;top:40px;font-size:10.5px;color:var(--cream)}
.social{position:absolute;right:23px;top:20px;display:flex;gap:13px}
.social a{width:17px;height:17px;border-radius:50%;background:var(--cream);display:block}
</style>
</head>
<body>
<div class="header-band"></div>
<div class="header-stripes"></div>

<div class="brand"><span class="brand-name">Torvell<br>Builders</span></div>
<div class="tagline">Your Project is out business!</div>
<div class="phone">
  <svg width="16" height="16" viewBox="0 0 24 24" aria-hidden="true"><path fill="#f4eddc" d="M6.6 10.8a15.2 15.2 0 0 0 6.6 6.6l2.2-2.2a1 1 0 0 1 1-.25 11.4 11.4 0 0 0 3.6.57 1 1 0 0 1 1 1V20a1 1 0 0 1-1 1A17 17 0 0 1 3 4a1 1 0 0 1 1-1h3.5a1 1 0 0 1 1 1c0 1.25.2 2.46.57 3.58a1 1 0 0 1-.25 1z"/></svg>
  555.214.0386
</div>

<nav class="main-nav">
  <a href="#" class="active">Home</a>
  <a href="#">Kitchen</a>
  <a href="#" class="open">Bath</a>
  <a href="#">Reviews</a>
  <a href="#">Portfolio</a>
  <a href="#">About</a>
  <a href="#">Contact</a>
</nav>
<div class="submenu">
  <a href="#">Residential</a>
  <a href="#">Commercial</a>
</div>

<div class="hero" role="img" aria-label="Warm kitchen with dark wood cabinets, granite island, pendant lights and steel refrigerator">
  <div class="hero-dots"><span></span><span class="on"></span><span></span><span></span></div>
</div>

<div class="banner">Commercial &amp; Residential General Construction Kitchen &amp; Bath Design</div>

<div class="estimate">
  <h2>Call today for a FREE estimate! 555.214.0386</h2>
  <p>Licensed - Bonded - Insured</p>
</div>

<section class="features">
  <div class="feature services">
    <h3>About Our Services</h3>
    <div class="photo" role="img" aria-label="Worker on a ladder in a kitchen under renovation" style="width:181px;height:138px;background:linear-gradient(180deg,#7a5a48,#b89a86 55%,#5c4236)"></div>
    <p>We have many different services to offer you to complete the dream design of your home.</p>
    <a href="#" class="more" style="left:3px;top:238px">Read more</a>
  </div>
  <div class="feature work">
    <h3>Our Work</h3>
    <div class="photo" role="img" aria-label="Bathroom with stone tile, soaking tub and glass shower" style="width:208px;height:138px;background:linear-gradient(180deg,#d9d4cc,#8a7462 50%,#5d4b3e)"></div>
    <p>We have various photos in our photo gallery displaying our work. We know you will not be disappointed!</p>
    <a href="#" class="more" style="left:1px;top:238px">Read more</a>
  </div>
  <div class="feature reviews">
    <h3>Testimonials</h3>
    <div class="photo" role="img" aria-label="Portrait of a satisfied client in his kitchen" style="width:207px;height:138px;border:1px solid var(--maroon);box-shadow:none;background:linear-gradient(180deg,#c8b48e,#8d7658 60%,#4a3e3a)"></div>
    <p class="quote">"I am very pleased with the level of support I received from this company. I recommend them to everyone! Thank you!"</p>
    <p class="author"><b>Marcus Delaney</b><br>Northfield Group, CEO</p>
  </div>
</section>

<footer class="footer">
  <nav class="footer-nav">
    <a href="#">Home</a><a href="#">Kitchen</a><a href="#">Bath</a><a href="#">Reviews</a><a href="#">Portfolio</a><a href="#">About</a><a href="#">Contact</a>
  </nav>
  <p class="copyright">Copyright © 2014 Torvell Builders. All rights reserved.</p>
  <div class="social">
    <a href="#" aria-label="Social profile"></a>
    <a href="#" aria-label="Social profile"></a>
    <a href="#" aria-label="Video channel"></a>
  </div>
</footer>
</body>
</html>
```